Harbour Blokes - community/social/support group for men needs a flyer

We need a flyer for our community group for display in GP clinics and other community services offices. Please refer to our website for design ideas: www.harbourblokes.org.au. We need it to be clean and simple to read.

Target Market(s)

Men 18+

Font styles to use
Serif

Colors
00a990

```html
<!DOCTYPE html>
<html lang="en">
<head>
<meta charset="utf-8">
<title>Harbour Blokes – Community Flyer</title>
<link rel="stylesheet" href="https://fonts.googleapis.com/css2?family=Oswald:wght@700&family=Roboto:wght@400;500;700&family=Open+Sans:wght@400;700&family=Montserrat:wght@500&display=swap">
<style>
  :root {
    --teal: #00a990;
    --teal-light: #14c9a8;
    --ink: #1e1e1e;
    --grey-light: #8c8c8c;
    --grey-dark: #3b3b3b;
    --page-bg: #d9d9d9;
    --white: #ffffff;
  }
  * { margin: 0; padding: 0; box-sizing: border-box; }
  html, body { width: 703px; height: 1200px; overflow: hidden; background: var(--page-bg); }
  .stage { position: relative; width: 703px; height: 1200px; }
  .flyer {
    position: absolute; left: 21px; top: 133px;
    width: 775px; height: 1095px;
    transform: scale(0.8516); transform-origin: 0 0;
    background: var(--white);
    box-shadow: 0 10px 30px rgba(0,0,0,.35);
    overflow: hidden;
    font-family: "Roboto", Arial, sans-serif;
  }
  .hero { position: absolute; left: 0; top: 0; width: 775px; height: 503px; }
  .hero-photo {
    position: absolute; inset: 0;
    background:
      radial-gradient(ellipse at 55% 30%, #6f8a4c 0%, transparent 55%),
      linear-gradient(160deg, #4f6b3a 0%, #7c8e57 35%, #b06a6a 65%, #c0545f 100%);
  }
  .hero-shapes { position: absolute; inset: 0; }
  .brand {
    position: absolute; right: 32px; top: 98px; width: 300px; text-align: center;
    font-family: "Montserrat", Arial, sans-serif; font-weight: 500;
    font-size: 25px; letter-spacing: .5px; color: var(--ink);
  }
  .headline {
    position: absolute; right: 43px; top: 240px; text-align: right;
    font-family: "Oswald", Impact, sans-serif; font-weight: 700;
    font-size: 60px; line-height: 62px; color: var(--white);
    text-transform: uppercase; letter-spacing: -.5px;
  }
  .intro {
    position: absolute; left: 0; top: 503px; width: 775px; height: 124px;
    background: linear-gradient(180deg, var(--grey-light) 0%, var(--grey-dark) 100%);
    padding: 20px 43px 0 43px;
    color: #f2f2f2; font-size: 12.6px; line-height: 15.8px;
    text-align: justify; text-align-last: center;
  }
  .intro .org { color: var(--teal); }
  .projects-title {
    position: absolute; left: 0; top: 650px; width: 775px; text-align: center;
    color: var(--teal); font-weight: 700; font-size: 22px; line-height: 23px;
  }
  .rule { position: absolute; left: 188px; top: 709px; width: 400px; height: 1px; background: #bdbdbd; }
  .rule-accent { position: absolute; left: 367px; top: 707px; width: 41px; height: 4px; background: var(--teal); }
  .project { position: absolute; width: 200px; margin-left: -100px; text-align: center; }
  .project svg { display: block; margin: 0 auto; width: 90px; height: 70px; }
  .project-label {
    font-family: "Open Sans", Arial, sans-serif; font-weight: 700;
    font-size: 12.8px; line-height: 13px; color: var(--ink); margin-top: 4px;
  }
  .project-more { font-family: "Open Sans", Arial, sans-serif; font-size: 12px; color: var(--teal); font-weight: 400; }
  .footer { position: absolute; left: 0; top: 1023px; width: 775px; height: 72px; }
  .footer-info {
    position: absolute; top: 12px; color: #f0f0f0; font-size: 10px; line-height: 11px;
  }
  .footer-info strong { display: block; font-size: 13px; line-height: 18px; font-weight: 500; color: var(--white); }
  .footer-divider { position: absolute; left: 346px; top: 18px; width: 1px; height: 36px; background: #e0e0e0; }
</style>
</head>
<body>
<div class="stage">
  <article class="flyer">
    <header class="hero">
      <div class="hero-photo" role="img" aria-label="Photo of three smiling men with arms around each other outdoors"></div>
      <svg class="hero-shapes" viewBox="0 0 775 503" preserveAspectRatio="none" aria-hidden="true">
        <defs>
          <linearGradient id="tealFade" x1="0" y1="0" x2="0" y2="1">
            <stop offset="0" stop-color="#13d3b0"/>
            <stop offset="1" stop-color="#00a990"/>
          </linearGradient>
        </defs>
        <polygon points="380,0 775,0 775,242 710,188 622,252" fill="#ffffff"/>
        <polygon points="250,503 710,188 775,242 775,503" fill="url(#tealFade)"/>
      </svg>
      <div class="brand">HARBOUR BLOKES</div>
      <h1 class="headline">Social<br>Support<br>Mateship<br>Community</h1>
    </header>

    <section class="intro">
      <p><span class="org">Harbour Blokes Inc.</span> is a community group that supports the positive activity, engagement and inclusion of men in the Greywater Bay district.&nbsp; Our aim is to reduce the number of men who are socially disadvantaged, marginalised or isolated to become productive, active members of the local community.&nbsp; We do this by providing opportunities for men (18 years+) to come together in open, non-judgemental, safe spaces and participate in a range of social activities that encourage new friendships, normalise help-seeking behaviours and link with local support services.</p>
    </section>

    <section class="projects">
      <h2 class="projects-title">WE RUN A NUMBER OF PROJECTS EACH YEAR<br>WHICH CURRENTLY INCLUDE</h2>
      <div class="rule"></div>
      <div class="rule-accent"></div>

      <svg width="1" height="1" style="position:absolute;left:0;top:0" aria-hidden="true">
        <defs>
          <linearGradient id="shadowFade" x1="1" y1="0" x2="0" y2="1">
            <stop offset="0" stop-color="#9a9a9a" stop-opacity=".7"/>
            <stop offset="1" stop-color="#ffffff" stop-opacity="0"/>
          </linearGradient>
          <g id="pin">
            <polygon points="45,8 14,38 45,62" fill="url(#shadowFade)"/>
            <polygon points="38,52 52,52 45,62" fill="#00a990"/>
            <circle cx="45" cy="30" r="29" fill="#00a990"/>
            <circle cx="45" cy="30" r="21" fill="#ffffff"/>
          </g>
        </defs>
      </svg>

      <div class="project" style="left:105px; top:742px;">
        <svg viewBox="0 0 90 70" aria-hidden="true"><use href="#pin"/>
          <rect x="36" y="24" width="8" height="14" fill="#1e1e1e"/><polygon points="35,24 40,18 45,24" fill="#1e1e1e"/>
          <path d="M46 38 L52 27 L55 38" stroke="#1e1e1e" stroke-width="2" fill="none"/></svg>
        <div class="project-label">Dads and kids<br>playgroup</div>
      </div>
      <div class="project" style="left:294px; top:742px;">
        <svg viewBox="0 0 90 70" aria-hidden="true"><use href="#pin"/>
          <circle cx="45" cy="30" r="13" fill="#1e1e1e"/>
          <rect x="37" y="26" width="16" height="8" rx="4" fill="#ffffff"/></svg>
        <div class="project-label">Games Night</div>
      </div>
      <div class="project" style="left:492px; top:742px;">
        <svg viewBox="0 0 90 70" aria-hidden="true"><use href="#pin"/>
          <circle cx="38" cy="23" r="3" fill="#1e1e1e"/><circle cx="45" cy="21" r="3" fill="#1e1e1e"/><circle cx="52" cy="23" r="3" fill="#1e1e1e"/>
          <rect x="34" y="28" width="22" height="4" fill="#1e1e1e"/>
          <rect x="35" y="32" width="3" height="8" fill="#1e1e1e"/><rect x="43.5" y="32" width="3" height="8" fill="#1e1e1e"/><rect x="52" y="32" width="3" height="8" fill="#1e1e1e"/></svg>
        <div class="project-label">Yarning Circle<br>(men’s discussion group)</div>
      </div>
      <div class="project" style="left:685px; top:742px;">
        <svg viewBox="0 0 90 70" aria-hidden="true"><use href="#pin"/>
          <circle cx="46" cy="30" r="10" fill="none" stroke="#1e1e1e" stroke-width="2.5"/>
          <circle cx="46" cy="30" r="5" fill="#1e1e1e"/>
          <rect x="33" y="21" width="2" height="18" fill="#1e1e1e"/><rect x="57" y="21" width="2" height="18" fill="#1e1e1e"/></svg>
        <div class="project-label" style="margin-top:7px;">GBTIQ+<br>social dinners</div>
      </div>

      <div class="project" style="left:193px; top:880px;">
        <svg viewBox="0 0 90 70" aria-hidden="true"><use href="#pin"/>
          <circle cx="40" cy="24" r="5" fill="none" stroke="#1e1e1e" stroke-width="2"/>
          <rect x="47" y="21" width="9" height="7" fill="#1e1e1e"/>
          <rect x="34" y="32" width="22" height="3" fill="#1e1e1e"/><rect x="34" y="37" width="22" height="3" fill="#1e1e1e"/></svg>
        <div class="project-label">Shared Services<br>working bee’s</div>
      </div>
      <div class="project" style="left:400px; top:880px;">
        <svg viewBox="0 0 90 70" aria-hidden="true"><use href="#pin"/>
          <circle cx="45" cy="24" r="5" fill="#1e1e1e"/>
          <path d="M36 36 Q45 26 54 36 Z" fill="#1e1e1e"/>
          <rect x="34" y="36" width="22" height="4" fill="#1e1e1e"/></svg>
        <div class="project-label">Guest speakers</div>
      </div>
      <div class="project" style="left:600px; top:880px;">
        <svg viewBox="0 0 90 70" aria-hidden="true"><use href="#pin"/>
          <circle cx="38" cy="25" r="3.5" fill="#1e1e1e"/><circle cx="45" cy="22" r="3.5" fill="#1e1e1e"/><circle cx="52" cy="25" r="3.5" fill="#1e1e1e"/>
          <circle cx="41" cy="33" r="3.5" fill="#1e1e1e"/><circle cx="49" cy="33" r="3.5" fill="#1e1e1e"/>
          <rect x="35" y="37" width="20" height="3" fill="#1e1e1e"/></svg>
        <div class="project-label">Annual men’s<br>gathering<br><span class="project-more">And more...</span></div>
      </div>
    </section>

    <footer class="footer">
      <svg viewBox="0 0 775 72" width="775" height="72" style="position:absolute;left:0;top:0" aria-hidden="true">
        <defs>
          <linearGradient id="footFade" x1="0" y1="0" x2="0" y2="1">
            <stop offset="0" stop-color="#8c8c8c"/>
            <stop offset="1" stop-color="#3b3b3b"/>
          </linearGradient>
        </defs>
        <polygon points="0,0 645,0 708,72 0,72" fill="url(#footFade)"/>
        <polygon points="693,50 775,50 775,72 712,72" fill="#00a990"/>
      </svg>
      <div class="footer-info" style="left:32px;">For a list of our current activities and to find our how you can get<br>involved, please visit us: online at:<strong>www.harbourblokes.org.au</strong></div>
      <div class="footer-divider"></div>
      <div class="footer-info" style="left:372px; top:20px;">join our Community page for our latest updates:<strong>www.matesboard.com/harbourblokesAU</strong></div>
    </footer>
  </article>
</div>
</body>
</html>
```